Business Card Design

as above
one side to be name of business and information about business inside an imessage text bubble.
other side to be contact details around an email icon . 'envelope'

Target Market(s)

seniors

Industry/Entity Type

Business

Contact Information for Business Card

Tap Along-Keep Along
Rosalind Parfrey
0438 617 204
Rosalind.tapalong@mailbeam.net
ABN:41870265913

Technology help for seniors in your own home.- tablets, music players, mobile phones, internet, email, computers. No question too small.

```html
<!DOCTYPE html>
<html lang="en">
<head>
<meta charset="utf-8">
<title>Tap Along-Keep Along – Business Card</title>
<link href="https://fonts.googleapis.com/css2?family=Nunito:wght@800&family=Questrial&display=swap" rel="stylesheet">
<style>
  :root {
    --backdrop: #dcdcdc;
    --navy: #0a2a44;
    --deep: #0f4a72;
    --ocean: #1a6e9e;
    --sky: #2fa8dc;
    --cyan: #3cc4f0;
    --band: rgba(74, 196, 240, 0.78);
    --ink: #1a1a1a;
    --services: #1b78b0;
    --name-blue: #2a9ad6;
    --env-dark: #1d7fc0;
    --env-mid: #3aa3dd;
    --env-side: #46ade4;
    --env-light: #5cbcec;
    --paper: #ffffff;
  }
  * { box-sizing: border-box; margin: 0; padding: 0; }
  html, body {
    width: 1200px; height: 900px; overflow: hidden;
    background: var(--backdrop);
  }
  .stage {
    position: relative; width: 1200px; height: 900px;
    display: flex; align-items: center; justify-content: center; gap: 60px;
  }
  .card {
    position: relative; width: 520px; height: 300px;
    border-radius: 22px; overflow: hidden;
    box-shadow: 0 14px 30px rgba(0,0,0,0.18);
  }

  /* Front side */
  .card-front { background: var(--navy); }
  .front-pattern {
    position: absolute; inset: 0;
    background:
      radial-gradient(ellipse 60% 70% at 92% 12%, rgba(60,196,240,0.75), transparent 70%),
      radial-gradient(ellipse 55% 60% at 70% 95%, rgba(47,168,220,0.6), transparent 70%),
      radial-gradient(ellipse 45% 55% at 10% 85%, rgba(26,110,158,0.7), transparent 70%),
      radial-gradient(ellipse 40% 40% at 45% 30%, rgba(26,110,158,0.55), transparent 70%),
      linear-gradient(120deg, var(--navy) 0%, var(--deep) 35%, var(--ocean) 65%, var(--sky) 100%);
  }
  .title-band {
    position: absolute; left: 0; right: 0; top: 66px; height: 48px;
    background: var(--band);
    border-bottom: 3px solid rgba(10,42,68,0.55);
    display: flex; align-items: center; padding-left: 28px;
  }
  .business-name {
    font-family: "Nunito", sans-serif;
    font-size: 33px; font-weight: 800; color: #fff;
    text-shadow: 1px 2px 2px rgba(0,0,0,0.6);
    letter-spacing: -0.6px;
  }
  .message-bubble {
    position: absolute; left: 22px; top: 140px;
    width: 456px; height: 120px;
  }
  .message-bubble svg { position: absolute; inset: 0; }
  .bubble-text {
    position: relative; padding: 20px 14px 0 14px;
    font-family: "Questrial", sans-serif; color: var(--ink);
  }
  .tagline { font-size: 20px; line-height: 1.1; }
  .services { font-size: 14px; line-height: 1.2; color: var(--services); padding-left: 10px; }
  .reassurance { font-size: 18px; text-align: center; margin-top: 14px; }

  /* Back side */
  .card-back { background: var(--paper); }
  .envelope { position: absolute; inset: 0; }
  .letter {
    position: absolute; left: 105px; top: 52px; width: 310px; height: 118px;
    background: var(--paper);
    box-shadow: 0 1px 4px rgba(0,0,0,0.25);
    text-align: center;
    font-family: "Questrial", sans-serif; color: var(--ink);
    padding-top: 8px;
  }
  .contact-name { font-size: 17px; color: var(--name-blue); margin-bottom: 14px; }
  .contact-phone { font-size: 17px; line-height: 1.15; }
  .contact-email { font-size: 13.5px; line-height: 1.2; }
  .contact-abn { font-size: 12.5px; line-height: 1.2; }
  .envelope-front { position: absolute; inset: 0; }
</style>
</head>
<body>
<main class="stage">
  <section class="card card-front">
    <div class="front-pattern" role="img" aria-label="Decorative pattern of overlapping blue ovals"></div>
    <div class="title-band">
      <h1 class="business-name">Tap Along-Keep Along</h1>
    </div>
    <div class="message-bubble">
      <svg viewBox="0 0 456 120" width="456" height="120" aria-hidden="true">
        <defs>
          <linearGradient id="bubbleFill" x1="0" y1="0" x2="0" y2="1">
            <stop offset="0" stop-color="#8fe3fb"/>
            <stop offset="0.22" stop-color="#3fc6f1"/>
            <stop offset="1" stop-color="#2db7e9"/>
          </linearGradient>
        </defs>
        <path d="M14 2 H436 Q448 2 448 14 V96 Q448 106 444 110 L454 118 Q440 116 432 110 H14 Q2 110 2 98 V14 Q2 2 14 2 Z"
              fill="url(#bubbleFill)" stroke="#1d86c0" stroke-width="1.5"/>
      </svg>
      <div class="bubble-text">
        <p class="tagline">Technology help for seniors in your own home</p>
        <p class="services">tablets, music players, mobile phones, internet, email, computers.</p>
        <p class="reassurance">No question too small</p>
      </div>
    </div>
  </section>

  <section class="card card-back">
    <svg class="envelope" viewBox="0 0 520 300" width="520" height="300" aria-hidden="true">
      <rect x="82" y="118" width="356" height="158" fill="var(--env-dark)"/>
      <polygon points="82,118 260,34 438,118" fill="var(--env-mid)"/>
    </svg>
    <div class="letter">
      <p class="contact-name">Rosalind Parfrey</p>
      <p class="contact-phone">0438 617 204</p>
      <p class="contact-email">Rosalind.tapalong@mailbeam.net</p>
      <p class="contact-abn">ABN:41870265913</p>
    </div>
    <svg class="envelope-front" viewBox="0 0 520 300" width="520" height="300" aria-hidden="true">
      <polygon points="82,128 260,200 438,128 438,276 82,276" fill="var(--env-mid)"/>
      <polygon points="82,276 260,200 438,276" fill="var(--env-light)"/>
      <polygon points="82,128 260,200 82,276" fill="var(--env-side)"/>
    </svg>
  </section>
</main>
</body>
</html>
```